Amber Kettle Corp Business Card Design

Amber Kettle Corp is a local owner and operator of several coffee shops in Irving, TX. Google "Bean Harbor Plaza" for an example of one of our shops.We would like an image that is professional, but with a slight nod to the protestant religious nature of our backers.The name "Amber Kettle" is a play on the concept of "rivers of living water". It also conveys the concept of a "life of coffee". We desire to combine these concepts in the logo visualization, with the emphasis on the commercial side of the concept.

Target Market(s)

Upper class retail. No drive-through. Comfy lounges.

Industry/Entity Type

Coffee Shop

Contact Information for Business Card

Dale Fenwick
Chief Operating Officer
Amber Kettle Corp
(555) 417 2906
dale@amberkettle.example (address not yet active)

Requirements
Must have
• We do not have a logo yet. Need that as a part of the design.
• This needs to be original artwork. I need to own the art when the design is finished. I will look at submissions with stock artwork, but be advised that I will not accept the submission until original work is presented.

```html
<!DOCTYPE html>
<html lang="en">
<head>
<meta charset="utf-8">
<title>Amber Kettle Corp — Business Card</title>
<link rel="stylesheet" href="https://fonts.googleapis.com/css2?family=Questrial&display=swap">
<style>
  :root {
    --backdrop: #e8e2d8;
    --card-white: #fbfbfa;
    --ink-grey: #4a4440;
    --amber: #b9782f;
    --amber-deep: #6e4218;
    --amber-mid: #94602a;
    --amber-light: #b07a3c;
    --on-amber: #ffffff;
  }
  html, body {
    margin: 0;
    padding: 0;
    width: 736px;
    height: 1200px;
    overflow: hidden;
    background: var(--backdrop);
    font-family: "Questrial", sans-serif;
  }
  .sheet {
    width: 736px;
    height: 1200px;
    display: flex;
    flex-direction: column;
    align-items: center;
    justify-content: center;
    gap: 90px;
  }
  .card {
    position: relative;
    width: 600px;
    height: 343px;
    box-sizing: border-box;
    border-radius: 3px;
    box-shadow: 0 10px 28px rgba(60, 40, 20, 0.22);
  }
  .card--front {
    background: var(--card-white);
    color: var(--ink-grey);
  }
  .card--back {
    background: linear-gradient(150deg, var(--amber-deep) 0%, var(--amber-mid) 45%, var(--amber-light) 62%, var(--amber-mid) 80%, var(--amber-deep) 100%);
    color: var(--on-amber);
    display: flex;
    align-items: center;
    justify-content: center;
  }
  .brand {
    display: flex;
    align-items: center;
    gap: 12px;
    font-size: 19px;
    letter-spacing: 5px;
  }
  .brand__dot {
    width: 12px;
    height: 12px;
    border-radius: 50%;
    background: currentColor;
    flex: none;
  }
  .card--front .brand {
    position: absolute;
    top: 78px;
    left: 0;
    right: 0;
    justify-content: center;
    color: var(--ink-grey);
  }
  .card--back .brand {
    font-size: 30px;
    letter-spacing: 7px;
    gap: 16px;
  }
  .card--back .brand__dot { width: 16px; height: 16px; }
  .person {
    position: absolute;
    top: 150px;
    left: 0;
    right: 0;
    text-align: center;
  }
  .person__name {
    margin: 0;
    font-size: 32px;
    font-weight: 400;
    color: var(--ink-grey);
  }
  .person__title {
    margin: 6px 0 0;
    font-size: 18px;
    color: var(--amber);
  }
  .contacts {
    position: absolute;
    bottom: 48px;
    left: 0;
    right: 0;
    display: flex;
    justify-content: center;
    gap: 48px;
    font-size: 16px;
    color: var(--ink-grey);
  }
  .contact {
    display: flex;
    align-items: center;
    gap: 8px;
  }
  .contact__icon {
    width: 18px;
    height: 18px;
    fill: var(--amber);
    flex: none;
  }
</style>
</head>
<body>
<main class="sheet">
  <section class="card card--front" aria-label="Card front">
    <div class="brand"><span class="brand__dot"></span><span class="brand__name">Amber Kettle Corp</span></div>
    <div class="person">
      <h1 class="person__name">Dale Fenwick</h1>
      <p class="person__title">Chief Operating Officer</p>
    </div>
    <div class="contacts">
      <div class="contact">
        <svg class="contact__icon" viewBox="0 0 24 24" aria-hidden="true">
          <path d="M3 7c0-2 2-3 9-3s9 1 9 3v2h-4V7.5c-1-.6-3-.9-5-.9s-4 .3-5 .9V9H3z"/>
          <path d="M6 11h12l2 9H4z M12 13.5a2.5 2.5 0 1 0 0 5a2.5 2.5 0 1 0 0-5z" fill-rule="evenodd"/>
        </svg>
        <span>(555) 417 2906</span>
      </div>
      <div class="contact">
        <svg class="contact__icon" viewBox="0 0 24 24" aria-hidden="true">
          <path d="M2 5h20v14H2z M3.5 6.5 12 13l8.5-6.5z" fill-rule="evenodd"/>
        </svg>
        <span>dale@amberkettle.example</span>
      </div>
    </div>
  </section>

  <section class="card card--back" aria-label="Card back">
    <div class="brand"><span class="brand__dot"></span><span class="brand__name">Amber Kettle Corp</span></div>
  </section>
</main>
</body>
</html>
```